11 x 11 Flyer Design for Social Media - Reverse Mortgages

62 or older?

A Reverse Mortgage
could be
Your Road to Financial Freedom

* No Monthly Payments
* No Income Requirements
* No Credit Score Requirements
* No Loss of Ownership

Receive cash by lump sum, monthly installments or a line of credit!!

Call us today for a Free Consultation!!
(800) 471-2965

Bluegate Financial Services, Inc.
NMLS #318760
www.bluegatehome.com

```html
<!DOCTYPE html>
<html lang="en">
<head>
<meta charset="utf-8">
<title>Reverse Mortgage – Bluegate Financial Services</title>
<link rel="stylesheet" href="https://fonts.googleapis.com/css2?family=Montserrat:ital,wght@0,300;0,400;0,500;0,600;0,700;1,500&display=swap">
<style>
  :root {
    --teal: #17989d;
    --teal-light: #9fd3d5;
    --yellow: #f6ee4b;
    --purple: #961a80;
    --grey: #8a8a8a;
    --ink: #111111;
    --white: #ffffff;
    --sea-top: #c9dced;
    --sea-mid: #6f98bf;
    --sea-low: #2e4d75;
  }
  * { margin: 0; padding: 0; box-sizing: border-box; }
  html, body { width: 1200px; height: 1200px; overflow: hidden; background: var(--white); }
  .flyer {
    position: relative;
    width: 1200px;
    height: 1200px;
    overflow: hidden;
    background: var(--white);
    font-family: "Montserrat", Arial, sans-serif;
  }
  .age-panel {
    position: absolute; left: 0; top: 0; width: 546px; height: 437px;
    background: var(--teal); color: var(--yellow);
  }
  .age-number {
    position: absolute; left: 52px; top: -48px;
    font-size: 410px; font-weight: 300; line-height: 1; letter-spacing: -6px;
  }
  .age-question {
    position: absolute; left: 36px; top: 318px;
    font-size: 103px; font-weight: 300; line-height: 1; letter-spacing: -1px;
  }
  .hero-photo {
    position: absolute; left: 546px; top: 0; width: 654px; height: 437px;
    background: linear-gradient(180deg, var(--sea-top) 0%, var(--sea-mid) 45%, var(--sea-low) 100%);
  }
  .headline {
    position: absolute; left: 46px; top: 455px;
    font-size: 73px; font-weight: 700; color: var(--teal); line-height: 1; letter-spacing: -0.5px;
  }
  .subhead-lead {
    position: absolute; left: 232px; top: 560px;
    font-size: 46px; font-weight: 400; color: var(--grey); line-height: 1;
  }
  .subhead {
    position: absolute; left: 472px; top: 550px;
    font-size: 64px; font-weight: 400; color: var(--teal); line-height: 1.2;
  }
  .benefits { position: absolute; left: 0; top: 728px; list-style: none; width: 720px; }
  .benefit {
    position: relative; height: 53px; margin-bottom: 0;
    padding-left: 78px; display: flex; align-items: center;
    font-size: 39px; font-weight: 400; color: var(--teal); line-height: 1;
  }
  .benefit::before {
    content: ""; position: absolute; left: 40px; top: 50%;
    width: 20px; height: 20px; margin-top: -10px; border-radius: 50%; background: var(--teal);
  }
  .benefit--band {
    background: linear-gradient(90deg, var(--teal-light) 0%, rgba(159,211,213,0.55) 60%, rgba(255,255,255,0) 100%);
  }
  .payout {
    position: absolute; left: 758px; top: 724px; width: 442px; height: 203px;
    background: var(--purple);
    clip-path: polygon(8% 0, 100% 0, 100% 100%, 0 100%);
    display: flex; align-items: center; justify-content: flex-end;
    padding-right: 58px;
  }
  .payout-text {
    color: var(--white); font-style: italic; font-weight: 500;
    font-size: 30px; line-height: 1.2; text-align: right;
  }
  .couple-photo {
    position: absolute; left: 0; top: 932px; width: 330px; height: 268px;
    background: linear-gradient(180deg, #e9eef2 0%, #cdd9e2 40%, #eef2f4 100%);
    -webkit-mask-image: linear-gradient(90deg, #000 60%, transparent 100%);
    mask-image: linear-gradient(90deg, #000 60%, transparent 100%);
  }
  .cta {
    position: absolute; left: 350px; top: 966px;
    font-size: 37px; font-weight: 500; color: var(--ink); line-height: 1;
  }
  .phone {
    position: absolute; left: 470px; top: 1022px;
    font-size: 76px; color: var(--ink); line-height: 1;
  }
  .phone-area { font-weight: 300; }
  .phone-number { font-weight: 700; }
  .company {
    position: absolute; left: 336px; top: 1124px;
    font-size: 19px; font-weight: 600; color: var(--ink); line-height: 1.4;
  }
  .website {
    position: absolute; left: 768px; top: 1138px;
    font-size: 30px; font-weight: 500; color: var(--ink); line-height: 1;
  }
</style>
</head>
<body>
<main class="flyer">
  <section class="age-panel">
    <div class="age-number">62</div>
    <div class="age-question">or older?</div>
  </section>
  <div class="hero-photo" role="img" aria-label="Photo of a smiling senior couple taking a selfie by the sea"></div>

  <h1 class="headline">A Reverse Mortgage</h1>
  <span class="subhead-lead">could be</span>
  <p class="subhead">Your Road to<br>Financial Freedom</p>

  <ul class="benefits">
    <li class="benefit benefit--band">No Monthly Payments</li>
    <li class="benefit">No Income Requirements</li>
    <li class="benefit benefit--band">No Credit Score Requirements</li>
    <li class="benefit">No Loss of Ownership</li>
  </ul>

  <aside class="payout">
    <p class="payout-text">Receive cash by<br>lump sum,<br>monthly installments<br>or a line of credit!!</p>
  </aside>

  <div class="couple-photo" role="img" aria-label="Photo of a senior couple in white walking on the beach"></div>

  <p class="cta">Call us today for a Free Consultation!!</p>
  <p class="phone"><span class="phone-area">(800)</span> <span class="phone-number">471-2965</span></p>
  <p class="company">Bluegate Financial Services, Inc.<br>NMLS #318760</p>
  <p class="website">www.bluegatehome.com</p>
</main>
</body>
</html>
```